Letterhead for Business Law Firm

We need a letter head for our firm based on the design we have settled on and it is attached. Our clients are small and large businesses around the world, and our letterhead is used typically for formal legal purposes such as demand letters (accusing the recipient of doing bad things) or responding to demand letters. It may also be sent to regulators and other government agencies. So this needs to be tasteful, but a little edgy as well - we try to convey that we are a firm that is different - businesses and investors come to us for creative, quick advice, typically in high stress circumstances, and for our ability to work through high conflict situations, and rapid paced engagements.

Target Market(s)

Lawyers, business executives, investors, government regulators who may receive letters from this firm on behalf of its clients.

Industry/Entity Type

Business

Requirements
Must have
• The design and the firm's contact information:
• Thornvale Law Firm, P.C.
• 8172 SW 17th Ave
• Portland, OR 97058
• phone: 971 555 0147
• fax: 971 555 0182
• in what placement and how depicted (e.g. a phone icon instead of the word "phone") I leave to your creative ideas.
Nice to have
• design and information can be placed at the top, bottom and/or sides of the letter, and the design should be for a standard letter size paper - and can have a separate design for the second page.

```html
<!DOCTYPE html>
<html lang="en">
<head>
<meta charset="utf-8">
<title>Thornvale Law Firm, P.C. — Letterhead</title>
<link rel="stylesheet" href="https://fonts.googleapis.com/css2?family=Open+Sans:wght@300;400&display=swap">
<style>
  :root {
    --paper: #ffffff;
    --ink: #1a1618;
    --ink-soft: #3a3a3a;
    --watermark: #e2e2e2;
  }
  html, body {
    margin: 0;
    padding: 0;
    width: 1019px;
    height: 1200px;
    overflow: hidden;
    background: var(--paper);
  }
  .letterhead {
    position: relative;
    width: 1019px;
    height: 1200px;
    background: var(--paper);
    font-family: "Open Sans", Arial, sans-serif;
    color: var(--ink-soft);
  }
  .firm-name {
    position: absolute;
    top: 62px;
    left: 0;
    width: 100%;
    text-align: center;
    margin: 0;
    font-weight: 300;
    font-size: 50px;
    line-height: 80px;
    letter-spacing: 0.2em;
    text-indent: 0.2em;
    color: var(--ink);
  }
  .watermark-name {
    position: absolute;
    top: 555px;
    left: 0;
    width: 100%;
    text-align: center;
    font-weight: 300;
    font-size: 66px;
    line-height: 90px;
    letter-spacing: 0.2em;
    text-indent: 0.2em;
    color: var(--watermark);
    user-select: none;
  }
  .contact-line {
    position: absolute;
    top: 1135px;
    left: 0;
    width: 100%;
    display: flex;
    justify-content: center;
    gap: 16px;
    font-size: 14px;
    line-height: 20px;
    margin: 0;
    padding: 0;
    list-style: none;
  }
  .contact-line li {
    display: flex;
    align-items: center;
    gap: 4px;
  }
  .contact-icon {
    width: 11px;
    height: 11px;
    fill: var(--ink-soft);
  }
  .address-line {
    position: absolute;
    top: 1165px;
    left: 0;
    width: 100%;
    text-align: center;
    margin: 0;
    font-size: 14px;
    line-height: 20px;
    letter-spacing: 0.12em;
  }
</style>
</head>
<body>
  <main class="letterhead">
    <h1 class="firm-name">THORNVALE</h1>
    <div class="watermark-name" aria-hidden="true">THORNVALE</div>

    <ul class="contact-line">
      <li>
        <svg class="contact-icon" viewBox="0 0 12 12" aria-label="Phone"><path d="M2.5 0.8 4.3 2.6 3.4 4a6 6 0 0 0 4.6 4.6l1.4-.9 1.8 1.8-1.3 1.6C5.4 11 1 6.6 0.9 2.1Z"/></svg>
        971 555 0147
      </li>
      <li>
        <svg class="contact-icon" viewBox="0 0 12 12" aria-label="Fax"><rect x="3" y="1" width="6" height="4"/><rect x="1" y="5" width="10" height="5" rx="1"/></svg>
        971 555 0182
      </li>
      <li>
        <svg class="contact-icon" viewBox="0 0 12 12" aria-label="Email"><path d="M1 4.5 6 1.5l5 3V11H1Z"/><path d="M1.5 5 6 8l4.5-3" fill="none" stroke="#fff" stroke-width="1"/></svg>
        info@thornvale.com
      </li>
      <li>
        <svg class="contact-icon" viewBox="0 0 12 12" aria-label="Website"><circle cx="6" cy="6" r="5"/><path d="M1 6h10M6 1v10M6 1c-2.5 3-2.5 7 0 10M6 1c2.5 3 2.5 7 0 10" fill="none" stroke="#fff" stroke-width="0.8"/></svg>
        www.thornvale.com
      </li>
    </ul>
    <p class="address-line">8172 SW 17th Ave, Portland, OR 97058</p>
  </main>
</body>
</html>
```